brightfieldhope christian ministry

We need a logo and website design for a contemporary, non-denominational, christian teaching ministry in Australia.

Our audience is christian, 20-45, male and female. The vibe of the ministry is confident, charismatic, energetic, bold, modern yet grounded in biblical truth. Intelligent, humorous, authentic,

Non catholic, not gaudy, not slick, not bland, not overly traditional or liturgical.

We have an emphasis on the Pentecostal phenomena of God the Holy Spirit in dynamic encounter along with reverence for God the Father, God the Son and the Bible.

On the website, we'd like it to be possible for visitors to download audio/video files easily to their devices by clicking on tiles.

we'd like to have a forum for questions. Discussion Board.

we'd like to be able to incorporate bible study software like Lampwell study Guide.
we'd like to be able to have a blog.

we'd like images to be cool and stylised, not cheesy.

A couple of websites I like the look of are: www.cedarmount.example ; rvt.example.au ; www.harbourlightglobal.example ; www.onpath.example although these are much more comprehensive than our start up.

we would like to be able to combine Chirplet and Friendwall with website.

we'd like to be able to edit and upload files easily without too much technical know-how.

at present i don't have content, but am looking for look ideas
Updates

Target Market(s)

25-45 christians

Industry/Entity Type

Christian

Logo Text

BrightFieldHope

Number of Pages Required

5+ page

Requirements
Must have
• impact
• style
• I am not sure what coded/uncoded means, but I am not a techie. I want you to design me a website that I can then use and edit easily.
Nice to have
• arty aesthetic,
• simple, solitary, ability to feed from website to FW and CHIRPLET and put audio files into tunebox
Should not have
• overly catholic imagery
• cliche dove
• not too dreary

```html
<!DOCTYPE html>
<html lang="en">
<head>
<meta charset="utf-8">
<title>BrightFieldHope</title>
<link href="https://fonts.googleapis.com/css2?family=Raleway:wght@300;400;500;600;700&display=swap" rel="stylesheet">
<style>
:root{
  --red:#c8161d;
  --ink:#1e1e1e;
  --body:#6a6a6a;
  --panel:#f1efef;
  --band:#e8e7e7;
  --white:#ffffff;
  --footer:#000000;
  --footer-bar:#222222;
  --footer-text:#7d7d7d;
}
*{margin:0;padding:0;box-sizing:border-box}
html,body{width:1200px;height:2397px;overflow:hidden}
body{position:relative;background:var(--white);font-family:'Raleway',sans-serif;color:var(--ink)}
.abs{position:absolute}
.btn{position:absolute;display:flex;align-items:center;justify-content:center;background:var(--red);color:var(--white);font-size:13px;font-weight:500;height:26px}

/* header */
.site-header{left:0;top:0;width:1200px;height:53px;background:var(--white)}
.brand{left:229px;top:13px;font-size:21px;font-weight:600;color:var(--ink);display:flex;align-items:center;gap:6px}
.brand-dot{width:9px;height:9px;border-radius:50%;background:var(--red)}
.nav{top:20px;font-size:10px;color:#333}
.social-dot{top:24px;width:6px;height:6px;border-radius:50%;background:#222}
.menu{left:965px;top:18px;width:25px;height:18px}

/* hero */
.hero{left:0;top:53px;width:1200px;height:475px;background:linear-gradient(180deg,#4f95a5 0%,#9ea88a 22%,#e9a045 40%,#f6b83a 52%,#6a3a16 64%,#0c0704 72%,#050403 100%)}
.hero-title{left:229px;top:176px;color:var(--white);font-size:35px;line-height:45px;font-weight:400}
.hero-title span{display:block;font-weight:300}
.hero-text{left:229px;top:268px;width:290px;color:var(--white);font-size:13px;line-height:18px;font-weight:500}

/* intro */
.intro{left:296px;top:556px;width:610px;text-align:center;font-size:11.5px;line-height:17px;color:var(--body)}

/* features */
.features{left:0;top:685px;width:1200px;height:542px;background:var(--panel)}
.section-title{position:absolute;left:0;width:1200px;text-align:center;font-size:36px;font-weight:300;color:var(--ink)}
.card{position:absolute;top:779px;width:254px;height:395px;background:var(--white)}
.card-media{width:254px;height:181px}
.card-title{text-align:center;font-size:19px;font-weight:500;margin-top:26px}
.card-text{text-align:center;font-size:11.5px;line-height:17px;color:var(--body);padding:0 26px;margin-top:10px}

/* donation */
.donate-media{position:absolute}
.donate-panel{position:absolute;background:var(--panel)}
.panel-title{position:absolute;font-size:19px;font-weight:600}
.panel-text{position:absolute;font-size:11.5px;line-height:17px;color:var(--body)}
.amount{left:227px;top:1651px;width:300px;height:32px;border:1px solid #c9c9c9;background:var(--white);display:flex;align-items:center;justify-content:space-between;padding:0 12px;font-size:11px}
.monthly{left:227px;top:1686px;display:flex;align-items:center;gap:6px;font-size:8px;color:#444}
.monthly i{width:8px;height:8px;border:1px solid #aaa;background:var(--white)}

/* media */
.media-band{left:0;top:1787px;width:1200px;height:402px;background:var(--band)}
.tile{position:absolute;top:1883px;width:192px}
.tile-media{width:192px;height:144px;position:relative}
.play{position:absolute;left:78px;top:54px;width:36px;height:36px;border-radius:50%;background:rgba(255,255,255,.85)}
.play::after{content:"";position:absolute;left:14px;top:10px;border-left:12px solid #222;border-top:8px solid transparent;border-bottom:8px solid transparent}
.tile-text{text-align:center;font-size:11.5px;line-height:17px;color:var(--body);margin-top:22px}
.tile-text b{color:var(--ink);font-weight:600}
.pager{left:580px;top:2160px;font-size:8px;color:#c8c8c8}
.pager-box{left:966px;top:2155px;width:20px;height:20px;border:1px solid #cfcfcf}

/* footer */
.site-footer{left:0;top:2189px;width:1200px;height:160px;background:var(--footer)}
.foot-col{position:absolute;top:2226px;font-size:11px;line-height:20px;color:var(--footer-text)}
.foot-col h4{color:var(--white);font-size:11.5px;font-weight:600;margin-bottom:2px}
.footer-bar{left:0;top:2349px;width:1200px;height:48px;background:var(--footer-bar);color:#cfcfcf;font-size:10px;display:flex;align-items:center;justify-content:center}
</style>
</head>
<body>

<header class="abs site-header">
  <div class="abs brand">BrightFieldHope<span class="brand-dot"></span></div>
  <div class="abs nav" style="left:806px">forum</div>
  <div class="abs nav" style="left:851px">Contact us</div>
  <span class="abs social-dot" style="left:918px" aria-label="Friendwall"></span>
  <span class="abs social-dot" style="left:937px" aria-label="Chirplet"></span>
  <svg class="abs menu" viewBox="0 0 25 18" aria-label="Menu"><rect width="25" height="3.5" fill="#c8161d"/><rect y="7" width="25" height="3.5" fill="#c8161d"/><rect y="14" width="25" height="3.5" fill="#c8161d"/></svg>
</header>

<section>
  <div class="abs hero" role="img" aria-label="Three crosses silhouetted on a hill against a golden sunset sky"></div>
  <h1 class="abs hero-title">LOREM IPSUM<span>DOLOR SIT AMET</span></h1>
  <p class="abs hero-text">Lorem ipsum dolor sit amet, consectetur adipiscing elit, sed do eiusmod tempor incididunt ut labore et dolore magna aliqua.</p>
  <a class="btn" style="left:229px;top:336px;width:125px">More Details</a>
</section>

<section>
  <p class="abs intro">Lorem ipsum dolor sit amet, consectetur adipiscing elit, sed do eiusmod tempor incididunt ut labore et dolore magna aliqua. Ut enim ad minim veniam, quis nostrud exercitation ullamco laboris nisi ut aliquip ex ea commodo consequat. Lorem ipsum dolor sit amet, consectetur adipiscing elit, commodo consequat.</p>
  <a class="btn" style="left:538px;top:624px;width:123px">View More Details</a>
</section>

<section>
  <div class="abs features"></div>
  <h2 class="section-title" style="top:706px">LOREM IPSUM</h2>

  <article class="card" style="left:208px">
    <div class="card-media" role="img" aria-label="Lit candle beside an open book" style="background:linear-gradient(135deg,#3a2a45 0%,#6d5a70 45%,#e8c98c 70%,#caa66a 100%)"></div>
    <h3 class="card-title">Daily Devotional</h3>
    <p class="card-text">Lorem ipsum dolor sit amet, consectetur adipiscing elit, sed do eiusmod tempor incididunt ut labore et dolore magna aliqua. Ut enim ad minim veniam, quis nostrud exercitation ullamco laboris nisi ut aliquip ex ea</p>
  </article>
  <article class="card" style="left:474px">
    <div class="card-media" role="img" aria-label="Adult hand holding a small child's hand" style="background:linear-gradient(135deg,#2e4a24 0%,#6f8a4c 40%,#d9a98a 60%,#4d6a35 100%)"></div>
    <h3 class="card-title">Real Help</h3>
    <p class="card-text">Lorem ipsum dolor sit amet, consectetur adipiscing elit, sed do eiusmod tempor incididunt ut labore et dolore magna aliqua. Ut enim ad minim veniam, quis nostrud exercitation ullamco laboris nisi ut aliquip ex ea commodo consequat</p>
  </article>
  <article class="card" style="left:738px">
    <div class="card-media" role="img" aria-label="Person writing in a notebook beside a laptop" style="background:linear-gradient(135deg,#9a8f83 0%,#c9c2b6 45%,#e9e5dc 60%,#5a544e 100%)"></div>
    <h3 class="card-title">Blog</h3>
    <p class="card-text">Lorem ipsum dolor sit amet, consectetur adipiscing elit, sed do eiusmod tempor incididunt ut labore et dolore magna aliqua. Ut enim ad minim veniam, quis nostrud exercitation ullamco laboris nisi ut aliquip ex ea</p>
  </article>
  <a class="btn" style="left:273px;top:1136px;width:123px">View More Details</a>
  <a class="btn" style="left:538px;top:1136px;width:123px">View More Details</a>
  <a class="btn" style="left:798px;top:1136px;width:123px">View More Details</a>
</section>

<section>
  <h2 class="section-title" style="top:1282px">ONLINE DONATION</h2>

  <div class="donate-media" role="img" aria-label="Laptop showing a bible on screen on a wooden desk" style="left:208px;top:1366px;width:392px;height:178px;background:linear-gradient(120deg,#6a5a66 0%,#2a2328 40%,#8a4a2c 70%,#c9b9a8 100%)"></div>
  <div class="donate-panel" style="left:600px;top:1366px;width:390px;height:178px"></div>
  <svg class="abs" style="left:586px;top:1442px" width="14" height="26" viewBox="0 0 14 26"><polygon points="14,0 0,13 14,26" fill="#f1efef"/></svg>
  <h3 class="panel-title" style="left:621px;top:1391px">HOLY BIBLE IN ONLINE</h3>
  <p class="panel-text" style="left:621px;top:1418px;width:340px">Lorem ipsum dolor sit amet, consectetur adipiscing elit, sed do eiusmod tempor incididunt ut labore et dolore magna aliqua. Ut enim ad minim veniam, quis nostrud exercitation ullamco laboris nisi ut aliquip ex ea</p>
  <a class="btn" style="left:622px;top:1499px;width:123px">Online now</a>

  <div class="donate-panel" style="left:208px;top:1554px;width:392px;height:214px"></div>
  <div class="donate-media" role="img" aria-label="Hands passing a gift to another person" style="left:600px;top:1554px;width:390px;height:214px;background:linear-gradient(135deg,#3f5a72 0%,#7e92a6 35%,#c79a80 60%,#4a3a30 100%)"></div>
  <svg class="abs" style="left:600px;top:1648px" width="14" height="26" viewBox="0 0 14 26"><polygon points="0,0 14,13 0,26" fill="#f1efef"/></svg>
  <h3 class="panel-title" style="left:227px;top:1581px">GIVE TODAY</h3>
  <p class="panel-text" style="left:227px;top:1608px;width:350px">Lorem ipsum dolor sit amet, consectetur adipiscing elit, sed do eiusmod tempor incididunt ut labore e.</p>
  <div class="abs amount"><span>$ 75</span><span>USD</span></div>
  <div class="abs monthly"><i></i>Make this a monthly gift</div>
  <a class="btn" style="left:330px;top:1709px;width:123px">Give now</a>
</section>

<section>
  <div class="abs media-band"></div>
  <h2 class="section-title" style="top:1815px">MUSIC AND VIDEO</h2>

  <div class="tile" style="left:208px">
    <div class="tile-media" role="img" aria-label="Burst of warm light rays" style="background:radial-gradient(circle at 50% 50%,#f3d8a0 0%,#b2602a 35%,#2a130a 80%)"><span class="play"></span></div>
    <p class="tile-text"><b>Lorem ipsum dolor sit amet,</b><br>consectetur adipiscing elit Lorem ipsum dolor sit amet,</p>
  </div>
  <div class="tile" style="left:405px">
    <div class="tile-media" role="img" aria-label="Crucifix resting on an open book" style="background:linear-gradient(135deg,#2a2522 0%,#6a5e52 45%,#b6a894 70%,#3e3630 100%)"><span class="play"></span></div>
    <p class="tile-text"><b>Lorem ipsum dolor sit amet,</b><br>consectetur adipiscing elit Lorem ipsum dolor sit amet,</p>
  </div>
  <div class="tile" style="left:602px">
    <div class="tile-media" role="img" aria-label="Interior of a church with arches" style="background:linear-gradient(180deg,#4a2a18 0%,#a8643a 45%,#d99a5a 60%,#3a2014 100%)"><span class="play"></span></div>
    <p class="tile-text"><b>Lorem ipsum dolor sit amet,</b><br>consectetur adipiscing elit Lorem ipsum dolor sit amet,</p>
  </div>
  <div class="tile" style="left:798px">
    <div class="tile-media" role="img" aria-label="Open bible on a lectern" style="background:linear-gradient(180deg,#d8d4d0 0%,#8e8680 45%,#3a302a 75%,#7a6a5a 100%)"><span class="play"></span></div>
    <p class="tile-text"><b>Lorem ipsum dolor sit amet,</b><br>consectetur adipiscing elit Lorem ipsum dolor sit amet,</p>
  </div>
  <a class="btn" style="left:243px;top:2104px;width:123px">Download</a>
  <a class="btn" style="left:440px;top:2104px;width:123px">Download</a>
  <a class="btn" style="left:636px;top:2104px;width:123px">Download</a>
  <a class="btn" style="left:832px;top:2104px;width:123px">Download</a>
  <div class="abs pager">Page 1</div>
  <svg class="abs pager-box" viewBox="0 0 20 20"><polyline points="8,6 12,10 8,14" fill="none" stroke="#bbb" stroke-width="1.2"/></svg>
</section>

<footer>
  <div class="abs site-footer"></div>
  <div class="foot-col" style="left:210px;width:230px"><h4>Address</h4>consectetur adipiscing elit Lorem ipsum dolor sit amet, Lorem ipsum dolor Lorem ipsum dolor sit amet,</div>
  <div class="foot-col" style="left:478px"><h4>Stay Connected</h4>Friendwall<br>Chirplet<br>Podcast<br>Netlink</div>
  <div class="foot-col" style="left:650px"><h4>Quick Links</h4>Home<br>About Us<br>Blog<br>Partner</div>
  <div class="foot-col" style="left:778px;font-size:10px"><h4>Latest News</h4>• Planning Your New Year Prayer Retreat<br>• What Does It Mean to "Renew My Mind?"<br>• How to watch the HFCN Broadcast<br>&nbsp;&nbsp;via Podcast</div>
  <div class="abs footer-bar">Copyright © 2017</div>
</footer>

</body>
</html>
```